Website redesign: OLU - Bright Reel Studio

Web Design Brief
I'm looking for a redesign of our website https://www.brightreel.studio/. The website is built with Wix.

We are an AI Video Production Agency named OLU that uses AI-technology to create videos for our clients. We use the platform vormetric.io to generate videos.

Use case:
A financial services company is looking for a way to transform their inhouse training content to video.
They visit brightreel.studio and submit a brief.
Several production packages are presented, and the company selects the one that suits them best. Pricing is agreed upon, and the company provides the necessary scripts and documentation.

As a growing agency, our web page's primary objective is to acquire business leads (companies seeking professional video services) and to communicate our unique AI-driven approach to video production. The landing page will include a form for potential clients to fill out their requirements, as well as a showcase of our AI's capabilities in video production.

We have not yet chosen a color palette, but we are looking for a design that will inspire confidence in our clients while also highlighting the innovative and creative nature of our service. The overall theme should be sleek, modern, and visual, as our core offering is video creation and editing.

Current website:
https://www.brightreel.studio/

Competitors:
https://www.clipforge.pro/
https://pixelbound.ai/
https://www.quillspots.com/vormetric

Inspiration:
https://www.vormetric.io/
https://lumo.co.uk/
https://crispnorth.co/
https://www.bluefennel.com/

Target Market(s)

Director's of training and others who work with video at companies with $10M+ in revenue and 100+ employees.

Industry/Entity Type

Video Services Agency

Coding

Coded - Design and coding required

Number of Pages Required

1 page

Font styles to use
Sans Serif

Requirements
Must have
• Clear CTA and services showcase above the fold. Include "Services" and "Blog" section.
Nice to have
• Reviews / Proof of concept

```html
<!DOCTYPE html>
<html lang="en">
<head>
<meta charset="UTF-8">
<title>OLU - Bright Reel Studio</title>
<link rel="stylesheet" href="https://fonts.googleapis.com/css2?family=Poppins:wght@400;500;600&display=swap">
<style>
  :root {
    --ink: #141a1f;
    --muted: #3b4248;
    --brand-blue: #2a6db5;
    --logo-blue: #2b7fc0;
    --bg-mint: #dff3ef;
    --bg-cyan: #d8f0f4;
    --bg-cream: #f7fbe8;
    --bg-lime: #eef8d6;
    --white: #ffffff;
    --video-dark: #1d2a2c;
    --video-warm: #6b5a3f;
  }
  * { box-sizing: border-box; margin: 0; padding: 0; }
  html, body { width: 1200px; height: 675px; overflow: hidden; }
  body {
    font-family: "Poppins", sans-serif;
    color: var(--ink);
    background:
      linear-gradient(120deg, transparent 46%, rgba(255,255,255,0.55) 56%, transparent 68%),
      linear-gradient(100deg, var(--bg-cyan) 0%, var(--bg-mint) 30%, var(--bg-cream) 60%, var(--bg-lime) 100%);
    position: relative;
  }
  .site-header {
    position: absolute;
    left: 47px; top: 36px;
    width: 1101px; height: 60px;
    border-radius: 30px;
    background: linear-gradient(90deg, rgba(232,246,240,0.95), rgba(245,250,228,0.95));
    box-shadow: 0 10px 22px rgba(90,110,80,0.18);
    display: flex; align-items: center; justify-content: space-between;
    padding: 0 32px 0 14px;
  }
  .brand { display: flex; align-items: center; gap: 10px; }
  .brand-mark {
    width: 36px; height: 36px; border-radius: 50%;
    border: 3px solid var(--logo-blue);
  }
  .brand-name {
    font-weight: 600; font-size: 28px; letter-spacing: 2px;
    color: var(--logo-blue);
  }
  .main-nav { display: flex; gap: 22px; font-size: 14px; color: var(--muted); }
  .main-nav a { color: inherit; text-decoration: none; }
  .main-nav a.is-active { color: var(--brand-blue); }
  .hero {
    position: absolute; left: 0; top: 0; width: 1200px;
    text-align: center;
  }
  .hero-title {
    position: absolute; left: 250px; top: 178px; width: 700px;
    font-weight: 500; font-size: 34px; line-height: 51px;
  }
  .hero-lead {
    position: absolute; left: 200px; top: 354px; width: 800px;
    font-size: 11px; line-height: 21px; color: var(--muted);
  }
  .cta-button {
    position: absolute; left: 486px; top: 425px;
    width: 228px; height: 49px; border-radius: 25px;
    background: var(--white);
    box-shadow: 0 8px 20px rgba(120,150,110,0.25);
    display: flex; align-items: center; gap: 12px;
    padding-left: 7px;
    color: var(--brand-blue); font-weight: 600; font-size: 15px;
    text-decoration: none;
  }
  .cta-button svg { width: 38px; height: 38px; }
  .showreel {
    position: absolute; left: 178px; top: 505px;
    width: 843px; height: 266px;
    border-radius: 12px;
    background:
      radial-gradient(ellipse 22% 80% at 50% 60%, var(--video-warm) 0%, transparent 70%),
      linear-gradient(100deg, #2a2a22 0%, var(--video-dark) 40%, #22333a 70%, #3a4a4c 100%);
  }
</style>
</head>
<body>
  <header class="site-header">
    <div class="brand">
      <span class="brand-mark"></span>
      <span class="brand-name">OLU</span>
    </div>
    <nav class="main-nav">
      <a class="is-active" href="#">Home</a>
      <a href="#">Services</a>
      <a href="#">Training</a>
      <a href="#">Marketing</a>
      <a href="#">Blog</a>
      <a href="#">Contact</a>
    </nav>
  </header>

  <main class="hero">
    <h1 class="hero-title">Grow your business by improving operations efficiency through video powered by AI</h1>
    <p class="hero-lead">OLU levels up your training and marketing teams thanks to high-quality and efficient video production powered by AI. You will<br>combine the latest technology available with the most professional and human touch.</p>
    <a class="cta-button" href="#">
      <svg viewBox="0 0 38 38" aria-hidden="true">
        <circle cx="19" cy="19" r="19" fill="#2a6db5"/>
        <path d="M15 11 L27 19 L15 27 Z" fill="#ffffff"/>
      </svg>
      See it in action Now
    </a>
    <div class="showreel" role="img" aria-label="Showreel video: presenter in front of a night city skyline"></div>
  </main>
</body>
</html>
```